Classy, Elegant, Simple Business Card Design

Looking to have a classy, simple, and elegant design. Want a top notch designed business card. I really like the look of the new veltro credit card. I also like the design I attached. I am trying to reach 21-29 year old females for booking us for there wedding or event. We offer Disc Jockey Service, Photo Booth Rentals, and Uplighting .

Target Market(s)

21-28 year old females

Contact Information for Business Card

Has to have logo, website, email, and phone number

Font styles to use
Other font styles liked:
• open to font choice, modern, clean
Designer to choose
33a6d7
0791cd
0555a3
ffffff

Requirements
Must have
• Has to have logo, website, email, and phone number
Nice to have
• I really like the design of the new veltro credit card. I also included my logo and some designs I like
Should not have
• clutter or too much info

```html
<!DOCTYPE html>
<html lang="en">
<head>
<meta charset="utf-8">
<title>Tidewell Event Group – Business Card</title>
<link href="https://fonts.googleapis.com/css2?family=Montserrat:wght@400;500;600&display=swap" rel="stylesheet">
<style>
  :root {
    --navy: #143056;
    --royal: #0555a3;
    --azure: #0791cd;
    --sky: #33a6d7;
    --white: #ffffff;
    --ink: #3a3f47;
    --backdrop: #e9ecf0;
  }
  html, body {
    margin: 0;
    width: 1200px;
    height: 912px;
    overflow: hidden;
    background: var(--backdrop);
    font-family: "Montserrat", sans-serif;
  }
  .canvas { position: relative; width: 1200px; height: 912px; }
  .card {
    position: absolute;
    width: 600px;
    height: 343px;
    border-radius: 16px;
    overflow: hidden;
    box-shadow: 0 10px 30px rgba(20, 48, 86, 0.18);
  }
  /* Back of card */
  .card--back { left: 150px; top: 74px; background: var(--navy); color: var(--white); }
  .card--back .brand {
    position: absolute; left: 0; right: 0; top: 130px;
    text-align: center; font-weight: 500; font-size: 34px; letter-spacing: 3px;
    color: var(--sky);
  }
  .card--back .brand-sub {
    position: absolute; left: 0; right: 0; top: 178px;
    text-align: center; font-weight: 500; font-size: 13px; letter-spacing: 6px;
    color: var(--sky);
  }
  .card--back .web {
    position: absolute; left: 0; right: 0; bottom: 38px;
    text-align: center; font-size: 15px; letter-spacing: 2px; color: var(--white);
  }
  /* Front of card */
  .card--front { left: 450px; top: 452px; background: var(--white); color: var(--ink); }
  .front-brand {
    position: absolute; left: 40px; top: 64px;
    font-weight: 600; font-size: 30px; letter-spacing: 1.5px; color: var(--royal);
    line-height: 1.15;
  }
  .front-brand small { display: block; font-size: 12px; letter-spacing: 5px; }
  .person { position: absolute; right: 36px; top: 52px; text-align: right; }
  .person .name { font-weight: 600; font-size: 22px; color: var(--royal); letter-spacing: 0.5px; }
  .person .role { font-size: 13px; color: var(--ink); margin-top: 2px; }
  .divider { position: absolute; left: 230px; right: 30px; top: 132px; height: 1.5px; background: var(--azure); }
  .address {
    position: absolute; right: 36px; top: 150px; text-align: right;
    font-size: 13px; line-height: 1.55; color: var(--ink);
  }
  .contacts {
    position: absolute; left: 40px; top: 212px; margin: 0; padding: 0; list-style: none;
    font-size: 14px; line-height: 1.75; color: var(--ink);
  }
  .contacts li { display: flex; align-items: center; gap: 10px; }
  .contacts svg { width: 12px; height: 12px; fill: none; stroke: var(--royal); stroke-width: 2; }
  .contacts .domain { color: var(--royal); font-weight: 600; }
  .front-band { position: absolute; left: 0; bottom: 0; width: 600px; height: 90px; }
</style>
</head>
<body>
<div class="canvas">
  <section class="card card--back" aria-label="Business card back">
    <div class="brand">TIDEWELL</div>
    <div class="brand-sub">EVENT GROUP</div>
    <div class="web">www.tidewellevents.com</div>
  </section>

  <section class="card card--front" aria-label="Business card front">
    <div class="front-brand">TIDEWELL<small>EVENT GROUP</small></div>
    <div class="person">
      <div class="name">DANIEL REYES</div>
      <div class="role">Managing Partner</div>
    </div>
    <div class="divider"></div>
    <div class="address">418 Harbor View Ave.<br>Los Angeles, CA 90012</div>
    <ul class="contacts">
      <li>
        <svg viewBox="0 0 12 12"><path d="M2.5 1.5 L4.5 1.5 L5.2 4 L4 5 C4.7 6.5 5.5 7.3 7 8 L8 6.8 L10.5 7.5 L10.5 9.5 C6 10 2 6 2.5 1.5 Z"/></svg>
        <span>615-555-0172</span>
      </li>
      <li>
        <svg viewBox="0 0 12 12"><rect x="1.5" y="3" width="9" height="6.5"/><path d="M1.5 3 L6 6.8 L10.5 3"/></svg>
        <span>info@tidewellevents.com</span>
      </li>
      <li>
        <svg viewBox="0 0 12 12"><circle cx="6" cy="6" r="4.5"/><path d="M1.5 6 H10.5 M6 1.5 C3.8 4 3.8 8 6 10.5 M6 1.5 C8.2 4 8.2 8 6 10.5"/></svg>
        <span>www.<span class="domain">tidewellevents</span>.com</span>
      </li>
    </ul>
    <svg class="front-band" viewBox="0 0 600 90" aria-hidden="true">
      <path d="M0 90 L0 80 L330 80 C362 80 372 62 388 44 C400 30 410 26 430 26 L600 26 L600 90 Z" fill="var(--navy)"/>
      <path d="M0 74 L325 74 C352 74 362 58 378 40 C390 26 402 20 425 20 L600 20 L600 23 L428 23 C407 23 397 29 384 44 C368 63 358 78 330 78 L0 78 Z" fill="var(--azure)"/>
    </svg>
  </section>
</div>
</body>
</html>
```